CREATIVE DESIGNERS NEEDED & Enhance Your Business Card Portfolio

Artistic, unique, professional real estate card needed - see attached documents "B-cards.pdf" for all details and examples.True Designers will see other projects of ours come online here. We like long-term relationships for creative designers. This business card will be used in two U.S. states and is central to our business and other future marketing.

Target Market(s)

Buyers and Sellers of real estate

Industry/Entity Type

Real Estate Agent

Contact Information for Business Card

See attached detailed brief

Font styles to use
Other font styles liked:
• ADAM.CG PRO & NewsGoth BT

Requirements
Must have
• 2-sided, creative (non-traditional layout/design). Incorporate a cut-out (for texture, and make it fun! No boring templates for this card -
Nice to have
• See attached detailed brief
Should not have

```html
<!DOCTYPE html>
<html lang="en">
<head>
<meta charset="UTF-8">
<title>Harbor Lane Group – Business Card</title>
<link rel="stylesheet" href="https://fonts.googleapis.com/css2?family=Work+Sans:wght@400;500;600&display=swap">
<style>
  :root {
    --page-bg: #e9e7e5;
    --card-bg: #1c1c1d;
    --card-bg-edge: #121213;
    --brand-red: #d0202a;
    --text-white: #f4f4f4;
    --text-soft: #cfcfcf;
    --photo-light: #6d7280;
    --photo-mid: #3a3c43;
  }
  * { box-sizing: border-box; margin: 0; padding: 0; }
  html, body {
    width: 1200px; height: 715px; overflow: hidden;
    background: var(--page-bg);
    font-family: "Work Sans", Arial, sans-serif;
  }
  .stage {
    width: 1200px; height: 715px;
    display: flex; align-items: center; justify-content: center; gap: 48px;
  }
  .card-shadow { filter: drop-shadow(0 10px 22px rgba(0,0,0,.28)); }
  .card {
    position: relative;
    width: 540px; height: 310px;
    background: linear-gradient(160deg, var(--card-bg) 0%, var(--card-bg-edge) 100%);
    border-radius: 6px;
    overflow: hidden;
    color: var(--text-white);
  }
  /* Die-cut notches: a half-circle punched into the facing edges of the pair */
  .card-front {
    -webkit-mask: radial-gradient(circle at 100% 50%, transparent 22px, #000 23px);
            mask: radial-gradient(circle at 100% 50%, transparent 22px, #000 23px);
  }
  .card-back {
    -webkit-mask: radial-gradient(circle at 0 50%, transparent 22px, #000 23px);
            mask: radial-gradient(circle at 0 50%, transparent 22px, #000 23px);
  }
  /* Angled die-cut corner */
  .card-front { clip-path: polygon(0 0, 100% 0, 100% 100%, 34px 100%, 0 calc(100% - 34px)); }
  .card-back  { clip-path: polygon(0 0, calc(100% - 34px) 0, 100% 34px, 100% 100%, 0 100%); }

  .brand { display: flex; align-items: center; gap: 12px; }
  .brand-square { width: 30px; height: 30px; background: var(--brand-red); flex: none; }
  .brand-name {
    font-weight: 600; font-size: 22px; line-height: 1.1;
    letter-spacing: .04em; text-transform: uppercase; color: var(--text-white);
  }

  /* Front */
  .card-front .portrait {
    position: absolute; left: 0; top: 0; bottom: 0; width: 290px;
    background:
      linear-gradient(90deg, transparent 55%, var(--card-bg) 100%),
      radial-gradient(ellipse 70% 80% at 45% 50%, var(--photo-light) 0%, var(--photo-mid) 60%, var(--card-bg) 100%);
  }
  .card-front .brand { position: absolute; left: 300px; top: 132px; }

  /* Back */
  .card-back .brand { position: absolute; left: 44px; top: 126px; }
  .card-back .divider {
    position: absolute; left: 268px; top: 62px; width: 2px; height: 186px;
    background: var(--brand-red);
  }
  .contact { position: absolute; left: 290px; top: 72px; right: 16px; }
  .contact-name {
    color: var(--brand-red); font-weight: 500; font-size: 23px;
    letter-spacing: .06em; text-transform: uppercase; white-space: nowrap;
  }
  .contact-title { font-size: 13px; color: var(--text-soft); margin: 2px 0 12px; }
  .contact-address { font-size: 13px; line-height: 1.4; margin-bottom: 8px; }
  .contact-list { list-style: none; }
  .contact-list li {
    display: flex; align-items: center; gap: 8px;
    font-size: 13px; line-height: 1.55; white-space: nowrap;
  }
  .contact-list svg { width: 10px; height: 10px; flex: none; }
</style>
</head>
<body>
<main class="stage">
  <div class="card-shadow">
    <section class="card card-front" aria-label="Card front">
      <div class="portrait" role="img" aria-label="Portrait photo of the agent"></div>
      <div class="brand">
        <span class="brand-square"></span>
        <span class="brand-name">Harbor Lane<br>Group</span>
      </div>
    </section>
  </div>

  <div class="card-shadow">
    <section class="card card-back" aria-label="Card back">
      <div class="brand">
        <span class="brand-square"></span>
        <span class="brand-name">Harbor Lane<br>Group</span>
      </div>
      <div class="divider"></div>
      <div class="contact">
        <p class="contact-name">Nolan Reyes</p>
        <p class="contact-title">Director</p>
        <p class="contact-address">218 Cedar Row West<br>Ashford, Ontario K2B 4M7</p>
        <ul class="contact-list">
          <li>
            <svg viewBox="0 0 10 10" aria-hidden="true"><path d="M2 1l2 2-1 1.2c.6 1.2 1.6 2.2 2.8 2.8L7 6l2 2-1.2 1.4C4.5 9 1 5.5.6 2.2z" fill="var(--brand-red)"/></svg>
            555-014-2236
          </li>
          <li>
            <svg viewBox="0 0 10 10" aria-hidden="true"><rect x=".8" y="2" width="8.4" height="6" fill="none" stroke="var(--brand-red)" stroke-width="1.2"/><path d="M.8 2L5 5.4 9.2 2" fill="none" stroke="var(--brand-red)" stroke-width="1.2"/></svg>
            info@harborlanegroup.com
          </li>
          <li>
            <svg viewBox="0 0 10 10" aria-hidden="true"><circle cx="5" cy="5" r="4.2" fill="none" stroke="var(--brand-red)" stroke-width="1.1"/><path d="M.8 5h8.4M5 .8c-2.2 2.4-2.2 6 0 8.4M5 .8c2.2 2.4 2.2 6 0 8.4" fill="none" stroke="var(--brand-red)" stroke-width=".9"/></svg>
            www.harborlanegroup.com
          </li>
        </ul>
      </div>
    </section>
  </div>
</main>
</body>
</html>
```